Halvering Family Dentistry
Peter K. Wadlow, DDS
Project: Halvering Family Dentistry
Halvering Family Dentistry -
Creative Brief
Professional
7182 Quillan Road, Unit C Charlottesville, VA 40317
smyle7q@postvale.net

```html
<!DOCTYPE html>
<html lang="en">
<head>
<meta charset="utf-8">
<title>Halvering Family Dentistry – Stationery</title>
<link rel="stylesheet" href="https://fonts.googleapis.com/css2?family=Lato:wght@400;700&display=swap">
<style>
:root{
  --backdrop:#e6d8c1;
  --paper:#ffffff;
  --brand-green:#3b8a3e;
  --deep-green:#2f7a33;
  --ink:#5a5a5a;
  --muted:#8a8a8a;
  --charcoal:#45484a;
  --label:#6b5a44;
}
*{box-sizing:border-box;margin:0;padding:0}
html,body{width:1200px;height:438px;overflow:hidden}
body{background:var(--backdrop);font-family:"Lato",sans-serif;color:var(--ink);position:relative}
.item{position:absolute;background:var(--paper);box-shadow:0 2px 5px rgba(0,0,0,.25)}
.item-label{position:absolute;font-size:6px;color:var(--label);text-align:center;width:160px}
.wordmark{font-family:"Lato",sans-serif;font-weight:700;color:var(--brand-green);line-height:1.1;display:flex;align-items:center;gap:5px;white-space:nowrap}
.wordmark .dot{width:8px;height:8px;border-radius:50%;background:var(--brand-green);flex:none}
.wordmark.small{font-size:7px}
.wordmark.small .dot{width:6px;height:6px}

/* presentation title */
.presentation-title{position:absolute;left:22px;top:86px;width:190px}
.presentation-title .wordmark{font-size:13px}
.presentation-title .tagline{font-size:5px;color:var(--muted);margin-top:5px;letter-spacing:.3px}
.presentation-title .concepts{font-size:7px;color:var(--charcoal);margin-top:4px;text-align:center}

/* business cards */
.card{width:144px;height:92px;padding:10px}
.card-front{left:24px;top:180px}
.card-back{left:24px;top:300px}
.card .holder{font-size:6px;font-weight:700;color:var(--deep-green);margin-top:12px;text-align:center}
.card .contact{font-size:4.5px;color:var(--muted);margin-top:10px;line-height:1.5}
.card-back .holder{margin-top:6px;text-align:left}

/* letterheads */
.letterhead{width:160px;height:378px;top:29px;padding:12px}
.letterhead-one{left:269px}
.letterhead-two{left:511px}
.letterhead .head{display:flex;justify-content:space-between;align-items:flex-start}
.letterhead .head-contact{font-size:4px;color:var(--muted);line-height:1.5}
.letterhead .footer{position:absolute;left:0;right:0;bottom:10px;text-align:center;font-size:3.5px;color:var(--muted)}

/* envelopes */
.envelope{left:835px;width:317px;height:85px;overflow:hidden}
.envelope svg{position:absolute;inset:0}
.env-charcoal{top:29px;background:var(--charcoal)}
.env-green{top:120px;background:var(--deep-green)}
.env-white{top:211px}
.env-front{left:804px;top:259px;width:355px;height:137px;padding:12px}
.env-front .footer{position:absolute;left:0;right:0;bottom:8px;text-align:center;font-size:4px;color:var(--muted)}
</style>
</head>
<body>

<section class="presentation-title">
  <div class="wordmark"><span class="dot"></span><span>Halvering Family Dentistry</span></div>
  <p class="tagline">GENTLE CARE FOR HEALTHY SMILES FOR LIFE</p>
  <p class="concepts">Stationery Concepts</p>
</section>

<article class="item card card-front">
  <div class="wordmark small" style="justify-content:center"><span class="dot"></span><span>Halvering Family Dentistry</span></div>
  <p class="holder">Peter K. Wadlow, DDS</p>
  <p class="contact">7182 Quillan Road, Unit C<br>(434) 555-0142<br>smyle7q@postvale.net</p>
</article>
<p class="item-label" style="left:16px;top:276px">Business card front</p>

<article class="item card card-back">
  <p class="holder">Peter K. Wadlow, DDS</p>
  <p class="contact">7182 Quillan Road, Unit C<br>Charlottesville, VA 40317<br>smyle7q@postvale.net</p>
  <div class="wordmark small" style="margin-top:6px"><span class="dot"></span><span>Halvering Family Dentistry</span></div>
</article>
<p class="item-label" style="left:16px;top:398px">Business card back</p>

<article class="item letterhead letterhead-one">
  <div class="head">
    <div class="wordmark small" style="font-size:6px"><span class="dot"></span><span>Halvering Family Dentistry</span></div>
    <p class="head-contact">7182 Quillan Road, Unit C<br>Charlottesville, VA 40317<br>Tel (434) 555-0142<br>Fax (434) 555-0143<br>smyle7q@postvale.net</p>
  </div>
</article>
<p class="item-label" style="left:269px;top:410px">Letterhead page one</p>

<article class="item letterhead letterhead-two">
  <div class="head" style="justify-content:center">
    <div class="wordmark small"><span class="dot"></span><span>Halvering Family Dentistry</span></div>
  </div>
  <p class="footer">7182 Quillan Road, Unit C · Charlottesville, VA 40317 · smyle7q@postvale.net</p>
</article>
<p class="item-label" style="left:511px;top:410px">Letterhead page two</p>

<div class="item envelope env-charcoal">
  <svg width="317" height="85"><path d="M0 0 L158 48 L317 0" fill="none" stroke="rgba(255,255,255,.25)" stroke-width="1"/></svg>
</div>
<div class="item envelope env-green">
  <svg width="317" height="85"><path d="M0 0 L158 48 L317 0 Z" fill="#eef3ee"/><path d="M0 0 L158 48 L317 0" fill="none" stroke="rgba(0,0,0,.15)"/></svg>
</div>
<div class="item envelope env-white">
  <svg width="317" height="85"><path d="M0 0 L158 48 L317 0" fill="none" stroke="#d3d3d3"/><path d="M0 85 L130 40 M317 85 L187 40" stroke="#e0e0e0"/></svg>
</div>
<article class="item env-front">
  <div class="wordmark small"><span class="dot"></span><span>Halvering Family Dentistry</span></div>
  <p class="footer">7182 Quillan Road, Unit C · Charlottesville, VA 40317</p>
</article>
<p class="item-label" style="left:900px;top:400px">Envelope set, back and front</p>

</body>
</html>
```